Visitenkarten-Design für Sonnen-/Fensterschutz
Zielgruppe
KLR GmbH ist eine Firma, die Sonnenschutz und Fensterschutz anbieten.
'Ihr kompetenter Partner in Sachen Sonnenschutz- , Fenster- und Türtechnik. Sie erhalten echtes Handwerk aus dem Mühlviertel zu fairen Preisen.'
Unsere Zielgruppe sind Personen mit Haus, die am Land leben.
Firmenname: KLR GmbH
Slogan: Fenster & Sonnenschutz
Aufgabenstellung
Hier befindet sich das Logodesign: https://dl.qv/t-Rm8pQ2wZtB
Bitte ein schlichtes Design bereitstellen mit einer Dummy-Person:
Lutz Brenneke + Telefonnummer + Email
Die finalen Daten bitte erst am Schluss berücksichtigen (für Gewinnerdesign)
Gerne auch hintern + vorne bedruckbar bereitstellen.

```html
<!DOCTYPE html>
<html lang="de">
<head>
<meta charset="utf-8">
<title>KLR GmbH – Visitenkarte</title>
<link rel="stylesheet" href="https://fonts.googleapis.com/css2?family=Open+Sans:wght@400;600;700&family=Poppins:wght@400&family=Orbitron:wght@700&display=swap">
<style>
  :root{
    --stage:#555555;
    --paper:#ffffff;
    --ink:#4a4a4a;
    --ink-soft:#5a5a5a;
    --muted:#8a8a8a;
    --orange:#ec6a1f;
    --red:#dc2a26;
    --brand-grad:linear-gradient(90deg,#ee7a1c 0%,#e85520 55%,#d9262a 100%);
    --photo-grad:linear-gradient(135deg,#e9e9e9 0%,#d6d6d6 60%,#c4c4c4 100%);
  }
  *{box-sizing:border-box;margin:0;padding:0}
  html,body{width:1200px;height:1200px;overflow:hidden;background:var(--stage)}
  .stage{position:relative;width:1200px;height:1200px}
  .card{position:absolute;left:286px;width:668px;height:433px;background:var(--paper);overflow:hidden}
  .card--front{top:97px}
  .card--back{top:603px}

  /* brand lockup */
  .brand{position:absolute;display:flex;flex-direction:column;align-items:flex-start}
  .brand__row{display:flex;align-items:center;gap:12px}
  .brand__mark{width:34px;height:34px;background:var(--red)}
  .brand__name{font-family:"Open Sans",sans-serif;font-weight:700;font-size:42px;line-height:1;color:var(--orange);letter-spacing:1px;white-space:nowrap}
  .brand__slogan{font-family:"Open Sans",sans-serif;font-weight:700;font-size:14px;color:var(--red);margin-top:6px;letter-spacing:.3px;white-space:nowrap}
  .card--front .brand{left:330px;top:46px}

  .brand--compact{left:30px;top:146px}
  .brand--compact .brand__row{gap:9px}
  .brand--compact .brand__mark{width:26px;height:26px}
  .brand--compact .brand__name{font-size:31px}
  .brand--compact .brand__slogan{font-size:11px;margin-top:5px}

  /* front */
  .person{position:absolute;left:0;width:330px;top:228px;text-align:center;font-family:"Open Sans",sans-serif}
  .person__name{font-size:26px;font-weight:400;color:var(--ink)}
  .person__role{font-size:18px;font-weight:600;color:var(--ink-soft);margin-top:2px}
  .divider{position:absolute;left:324px;top:168px;width:2px;height:170px;background:linear-gradient(180deg,rgba(236,106,31,0),var(--orange) 30%,var(--orange) 70%,rgba(236,106,31,0))}
  .contact{position:absolute;left:376px;top:178px;font-family:"Poppins",sans-serif;color:var(--ink);font-size:19.5px;line-height:1.28;list-style:none}
  .contact__company{padding-left:32px;color:var(--muted);font-size:17px;margin-bottom:6px}
  .contact__company b{font-family:"Open Sans",sans-serif;font-weight:700;font-size:19px;color:#9a9a9a;letter-spacing:1px}
  .contact__item{display:flex;align-items:flex-start;gap:8px;margin-bottom:14px}
  .contact__icon{width:24px;height:24px;flex:none;margin-top:1px}
  .accent-stripe{position:absolute;left:0;right:0;top:399px;height:12px;background:var(--brand-grad)}

  /* back */
  .photo{position:absolute;left:297px;top:0;width:371px;height:343px;background:var(--photo-grad)}
  .slogan-band{position:absolute;left:0;right:0;top:343px;height:90px;background:var(--brand-grad);display:flex;align-items:center;justify-content:center}
  .slogan-band__text{font-family:"Orbitron",sans-serif;font-weight:700;font-size:33px;letter-spacing:3px;color:#fbe3d6}
</style>
</head>
<body>
<main class="stage">

  <section class="card card--front" aria-label="Visitenkarte Vorderseite">
    <div class="brand">
      <div class="brand__row"><span class="brand__mark"></span><span class="brand__name">KLR GmbH</span></div>
      <span class="brand__slogan">FENSTER &amp; SONNENSCHUTZ</span>
    </div>

    <div class="person">
      <p class="person__name">Lutz Brenneke</p>
      <p class="person__role">Geschäftsführer</p>
    </div>

    <div class="divider"></div>

    <ul class="contact">
      <li class="contact__company"><b>KLR</b> GmbH</li>
      <li class="contact__item">
        <svg class="contact__icon" viewBox="0 0 24 24"><path d="M2 3 L22 12 L2 21 L7 12 Z" fill="var(--red)"/></svg>
        <span>Am Kastanienhof 21-23<br>30519 Hannover</span>
      </li>
      <li class="contact__item">
        <svg class="contact__icon" viewBox="0 0 24 24"><path d="M6 3 l3 0 l2 5 l-2.5 1.5 a11 11 0 0 0 6 6 l1.5 -2.5 l5 2 l0 3 a2 2 0 0 1 -2 2 A17 17 0 0 1 4 5 a2 2 0 0 1 2 -2z" fill="var(--red)"/></svg>
        <span>+49 152 408 3317</span>
      </li>
      <li class="contact__item">
        <svg class="contact__icon" viewBox="0 0 24 24"><rect x="2" y="6" width="20" height="14" rx="1.5" fill="var(--red)"/><path d="M2.5 7 L12 14 L21.5 7" fill="none" stroke="#fff" stroke-width="1.6"/></svg>
        <span>klrfenster@example.com</span>
      </li>
    </ul>

    <div class="accent-stripe"></div>
  </section>

  <section class="card card--back" aria-label="Visitenkarte Rückseite">
    <div class="brand brand--compact">
      <div class="brand__row"><span class="brand__mark"></span><span class="brand__name">KLR GmbH</span></div>
      <span class="brand__slogan">FENSTER &amp; SONNENSCHUTZ</span>
    </div>

    <div class="photo" role="img" aria-label="Foto einer gerollten Stoffbahn für Sonnenschutz mit Firmenaufdruck"></div>

    <div class="slogan-band">
      <span class="slogan-band__text">FENSTER &amp; SONNENSCHUTZ</span>
    </div>
  </section>

</main>
</body>
</html>
```